Banner Ad to drive users to the site

Hi I need a banner designed that promotes my website: www.nookmerra.com.au. It would need to be produced at two sizes one at 450 X 200 and the other at 225 X 100. The banner should be flash based.

The site is a local networking site, which basically means users can upload news, stories, articles, images and events to the website. The banner has to drive users to signup and want to interact with the site. The large banner will appear on the home page and the smaller banner on subsequent pages.

Texts that could be used in the banner are:
Write an Article and Post it Here
Post a Local News Story
Have a Picture of Your Street, Post It Here
Write an Article, Get Involved
Australia's Newest Local Networking Site
Get in touch with your Suburb
NookMerra - A glimpse of your Corner

images of house, streets, scenary, bridges (Wexcombe Quay Bridge, Tollan Pavilion) could be used in the animation.

The design should be modern but colourful (lacking color on the site at present) It should be not exceed 15 secs in animation and should loop. It should attract the users attention and end with a Click Here To Start

Please note I have now guaranteed this project.

Thanks
Brent

Target Market(s)

Mum and Dad users, Australians.

Requirements
Must have
• Colourful, but tasteful. Bold and to the point.
Should not have
• Too much colour, too much movement

```html
<!DOCTYPE html>
<html lang="en">
<head>
<meta charset="utf-8">
<title>NookMerra Banner Frames</title>
<link rel="stylesheet" href="https://fonts.googleapis.com/css2?family=Mulish:wght@400;700;800&family=Roboto+Condensed:wght@700&display=swap">
<style>
  :root {
    --canvas: #ffffff;
    --frame-edge: #2a2a2a;
    --panel-light: #ffffff;
    --panel-mid: #ececec;
    --panel-dark: #d2d2d2;
    --ink: #333333;
    --ink-black: #111111;
    --teal: #1a7a93;
    --band-top: #8a8a8a;
    --band-bottom: #111111;
    --btn-top: #f04848;
    --btn-mid: #d3171b;
    --btn-bottom: #a50b0f;
    --photo-skin: #d9b8a2;
    --photo-red: #c8352f;
    --photo-green: #8fc46a;
    --photo-silver: #cfd2d6;
  }
  * { box-sizing: border-box; margin: 0; padding: 0; }
  html, body {
    width: 1200px; height: 900px; overflow: hidden;
    background: var(--canvas);
  }
  .stage { position: relative; width: 1200px; height: 900px; }
  .banner {
    position: absolute; left: 308px; width: 584px; height: 258px;
    border: 1px solid var(--frame-edge);
    background: radial-gradient(ellipse 60% 80% at 60% 40%, var(--panel-light) 0%, var(--panel-mid) 60%, var(--panel-dark) 100%);
    overflow: hidden;
    font-family: "Mulish", Arial, sans-serif;
    color: var(--ink);
  }
  .banner--pictures { top: 31px; }
  .banner--news { top: 320px; }
  .banner--join { top: 607px; }
  .banner__band {
    position: absolute; left: 0; right: 0; bottom: 0; height: 16px;
    background: linear-gradient(var(--band-top), var(--band-bottom));
  }
  .photo { position: absolute; }
  .photo--man {
    left: 0; top: 18px; width: 330px; height: 224px;
    background: linear-gradient(90deg, var(--photo-red) 0%, var(--photo-red) 22%, var(--photo-skin) 45%, var(--photo-silver) 80%, rgba(207,210,214,0) 100%);
    opacity: .85;
    border-radius: 0 60px 0 0;
  }
  .photo--woman {
    right: 0; top: 20px; width: 300px; height: 222px;
    background: linear-gradient(270deg, var(--photo-green) 0%, var(--photo-green) 18%, var(--photo-skin) 40%, var(--photo-silver) 75%, rgba(207,210,214,0) 100%);
    opacity: .85;
    border-radius: 60px 0 0 0;
  }
  .headline {
    position: absolute; font-size: 34px; line-height: 40px; font-weight: 400;
    letter-spacing: -0.2px;
  }
  .headline strong { color: var(--teal); font-weight: 700; }
  .banner--pictures .headline { left: 210px; width: 360px; top: 52px; text-align: center; }
  .banner--news .headline { left: 46px; top: 48px; }
  .brand {
    position: absolute; top: 18px; left: 0; right: 0;
    display: flex; justify-content: center; align-items: center; gap: 8px;
  }
  .brand__mark { width: 26px; height: 26px; background: var(--ink-black); border-radius: 4px; }
  .brand__name { font-weight: 800; font-size: 34px; color: var(--ink-black); line-height: 1; }
  .brand__tagline {
    position: absolute; top: 62px; left: 0; right: 0; text-align: center;
    font-weight: 700; font-size: 15px; color: var(--ink-black);
  }
  .pitch {
    position: absolute; top: 96px; left: 0; right: 0; text-align: center;
    font-family: "Roboto Condensed", "Arial Narrow", sans-serif;
    font-weight: 700; font-size: 27px; color: var(--teal); letter-spacing: .5px;
  }
  .cta {
    position: absolute; left: 117px; top: 152px; width: 354px; height: 66px;
    border-radius: 6px;
    background: linear-gradient(var(--btn-top) 0%, var(--btn-mid) 50%, var(--btn-bottom) 100%);
    box-shadow: 3px 4px 6px rgba(0,0,0,.45);
    border: 1px solid #7d0a0c;
    display: flex; align-items: center; justify-content: center;
    font-family: "Roboto Condensed", "Arial Narrow", sans-serif;
    font-weight: 700; font-size: 31px; color: #ffffff;
    text-shadow: 1px 1px 2px rgba(0,0,0,.5);
    text-decoration: none;
  }
</style>
</head>
<body>
<div class="stage">
  <section class="banner banner--pictures">
    <div class="photo photo--man" role="img" aria-label="Man in a red t-shirt lying down, typing on a laptop"></div>
    <h2 class="headline">Upload <strong>Pictures</strong> of<br>Your Suburb</h2>
    <div class="banner__band"></div>
  </section>

  <section class="banner banner--news">
    <div class="photo photo--woman" role="img" aria-label="Woman in a green top lying down, typing on a laptop"></div>
    <h2 class="headline">Send Us Your Own<br><strong>News</strong> Story<br>or <strong>Article</strong></h2>
    <div class="banner__band"></div>
  </section>

  <section class="banner banner--join">
    <div class="brand">
      <span class="brand__mark"></span>
      <span class="brand__name">NookMerra</span>
    </div>
    <p class="brand__tagline">A Glimpse of Your Corner</p>
    <p class="pitch">Australia's Only Local Networking Site</p>
    <a class="cta" href="#">Click Here To Begin</a>
    <div class="banner__band"></div>
  </section>
</div>
</body>
</html>
```